Warning Sign

I need a new security warning sign creating in a new theme. I have uploaded an old sign to give you an idea. However, the details are different.

The sign must be very large and very high definition. It will be printed at 600mm x 400mm
Telephone Number is 0800 412 3967
Website is www.tvk-holdings.co.uk
Email is security@tvk-holdings.co.uk

The company name is called "TVK Security & Monitoring"

I have uploaded the new Logo, Letter Head and Business Card to give you an idea of the new theme.

List of Services is different to the old sign. They are as follows:

Static Security
Mobile Patrols
Alarm Response & Key Holding
Alarm & CCTV Monitoring
Welfare Hire

```html
<!DOCTYPE html>
<html lang="en">
<head>
<meta charset="utf-8">
<title>TVK Security &amp; Monitoring – Warning Sign</title>
<link rel="stylesheet" href="https://fonts.googleapis.com/css2?family=Exo+2:ital,wght@1,800&family=Lato:wght@700;900&display=swap">
<style>
  :root {
    --page: #eef1f5;
    --sky-blue: #1677cc;
    --mid-blue: #2148b8;
    --deep-blue: #16239a;
    --navy: #0e1a78;
    --accent: #2a9be8;
    --glow: #4fc3f7;
    --footer: #232427;
    --white: #ffffff;
  }
  * { box-sizing: border-box; margin: 0; padding: 0; }
  html, body {
    width: 1200px; height: 1120px; overflow: hidden;
    background: var(--page);
  }
  .sign {
    position: absolute; left: 40px; top: 186px;
    width: 1120px; height: 747px;
    overflow: hidden;
    box-shadow: 0 10px 30px rgba(0,0,0,.25);
    font-family: "Lato", sans-serif;
    color: var(--white);
  }
  .sign-backdrop { position: absolute; inset: 0; }
  .headline {
    position: absolute; right: 44px; top: 46px;
    font-family: "Exo 2", sans-serif; font-weight: 800; font-style: italic;
    font-size: 86px; letter-spacing: 2px; line-height: 1;
    text-shadow: 3px 4px 0 rgba(10,20,80,.55);
  }
  .brand {
    position: absolute; left: 70px; top: 250px;
    font-weight: 700; font-size: 52px; line-height: 1.05;
    color: var(--white);
  }
  .services {
    position: absolute; left: 70px; top: 400px;
    list-style: none;
  }
  .services li {
    display: flex; align-items: center; gap: 16px;
    font-weight: 700; font-size: 31px; line-height: 43px;
  }
  .services svg { width: 30px; height: 30px; flex: none; }
  .feature-art {
    position: absolute; left: 700px; top: 250px;
    width: 400px; height: 370px;
    border-radius: 50%;
    background: radial-gradient(circle at 50% 45%, rgba(79,195,247,.55) 0%, rgba(42,155,232,.35) 35%, rgba(33,72,184,0) 70%);
  }
  .footer-contact {
    position: absolute; left: 0; right: 0; top: 638px;
    text-align: center;
    font-weight: 700; font-size: 30px; line-height: 44px;
  }
</style>
</head>
<body>
  <main class="sign">
    <svg class="sign-backdrop" viewBox="0 0 1120 747" width="1120" height="747" aria-hidden="true">
      <defs>
        <linearGradient id="topBand" x1="0" y1="0" x2="0" y2="1">
          <stop offset="0" stop-color="#0f6fc6"/>
          <stop offset="1" stop-color="#1b82d6"/>
        </linearGradient>
        <radialGradient id="mainPanel" cx="0.35" cy="0.45" r="0.75">
          <stop offset="0" stop-color="#3452c8"/>
          <stop offset="0.6" stop-color="#1d2fa6"/>
          <stop offset="1" stop-color="#111d80"/>
        </radialGradient>
      </defs>
      <rect width="1120" height="620" fill="url(#topBand)"/>
      <path d="M0 250 C 50 150, 150 110, 300 112 C 520 115, 720 250, 900 300 C 990 325, 1060 330, 1120 322 L1120 620 L0 620 Z" fill="url(#mainPanel)"/>
      <path d="M150 122 C 300 70, 520 110, 720 210 C 880 290, 1000 320, 1120 300" fill="none" stroke="#0d1c7a" stroke-width="9"/>
      <rect y="610" width="1120" height="10" fill="var(--accent)"/>
      <rect y="620" width="1120" height="127" fill="var(--footer)"/>
    </svg>

    <div class="headline">WARNING</div>

    <div class="brand">TVK Security<br>&amp; Monitoring</div>

    <ul class="services">
      <li><svg viewBox="0 0 30 30"><circle cx="15" cy="15" r="14" fill="#fff"/><path d="M10.5 14v-3a4.5 4.5 0 0 1 9 0v3" fill="none" stroke="#16239a" stroke-width="2.4"/><rect x="8.5" y="13.5" width="13" height="10" rx="2" fill="#16239a"/></svg>Static Security</li>
      <li><svg viewBox="0 0 30 30"><circle cx="15" cy="15" r="14" fill="#fff"/><path d="M10.5 14v-3a4.5 4.5 0 0 1 9 0v3" fill="none" stroke="#16239a" stroke-width="2.4"/><rect x="8.5" y="13.5" width="13" height="10" rx="2" fill="#16239a"/></svg>Mobile Patrols</li>
      <li><svg viewBox="0 0 30 30"><circle cx="15" cy="15" r="14" fill="#fff"/><path d="M10.5 14v-3a4.5 4.5 0 0 1 9 0v3" fill="none" stroke="#16239a" stroke-width="2.4"/><rect x="8.5" y="13.5" width="13" height="10" rx="2" fill="#16239a"/></svg>Alarm Response &amp; Key Holding</li>
      <li><svg viewBox="0 0 30 30"><circle cx="15" cy="15" r="14" fill="#fff"/><path d="M10.5 14v-3a4.5 4.5 0 0 1 9 0v3" fill="none" stroke="#16239a" stroke-width="2.4"/><rect x="8.5" y="13.5" width="13" height="10" rx="2" fill="#16239a"/></svg>Alarm &amp; CCTV Monitoring</li>
      <li><svg viewBox="0 0 30 30"><circle cx="15" cy="15" r="14" fill="#fff"/><path d="M10.5 14v-3a4.5 4.5 0 0 1 9 0v3" fill="none" stroke="#16239a" stroke-width="2.4"/><rect x="8.5" y="13.5" width="13" height="10" rx="2" fill="#16239a"/></svg>Welfare Hire</li>
    </ul>

    <div class="feature-art" role="img" aria-label="Digital security illustration: a glowing shield with a keyhole above an open wireframe hand, ringed by small technology icons"></div>

    <div class="footer-contact">
      <p>Ph: 0800 412 3967 | www.tvk-holdings.co.uk</p>
      <p>Email is security@tvk-holdings.co.uk</p>
    </div>
  </main>
</body>
</html>
```